Wedding Videography Wordpress Website Theme

We need a modern and high-end website look for our wedding video and film business. We film weddings all over the United Kingdom and at European destinations so need something to reflect our work. The website should be visually stunning with images and videos being the focal point as this is what our services are.

The current website is www.brennolfside.com so you will be able to see our brand.

My Instagram is www.instagram.com/brennolfsidefilms so a new design should link in with this idea.

We need the following pages designed by the winning designer

1 - Homepage
2 - Films Index Page
3 - Testimonials
4 - Prices
5 - Reviews
6 - Meet Corin (About)
7 - Contact
8 - Blog Index
9 - Blog Page

All pages must be consistent so have a similar style.

Pages on menu:
Meet Corin
Videos
Packages
Testimionials
Journal (Blog)
Contact

We require a responsive look too. Over 90% of our visitors access the website via their mobile devices.

```html
<!DOCTYPE html>
<html lang="en">
<head>
<meta charset="utf-8">
<title>Corin Brennolfside Wedding Films</title>
<link href="https://fonts.googleapis.com/css2?family=Montserrat:wght@400;500;600&family=Lato:wght@400;700&family=Great+Vibes&display=swap" rel="stylesheet">
<style>
:root{
  --cream:#fdfaf1;
  --gold:#a68b4c;
  --gold-light:#c7ad6e;
  --brown:#3e342d;
  --brown-deep:#2f2823;
  --text:#4a423b;
  --white:#ffffff;
}
*{box-sizing:border-box;margin:0;padding:0}
html,body{width:1200px;height:4930px;overflow:hidden}
body{background:var(--cream);font-family:"Lato",sans-serif;color:var(--text);position:relative}
.abs{position:absolute}
.caps{font-family:"Montserrat",sans-serif}
.script{font-family:"Great Vibes",cursive;font-weight:400}

/* hero */
.hero{position:absolute;left:0;top:0;width:1200px;height:710px;background:linear-gradient(120deg,#6b4a38 0%,#b78f76 35%,#d9b9a3 50%,#3b2c27 75%,#1d1a1e 100%)}
.nav a{position:absolute;top:72px;color:var(--white);font-family:"Montserrat",sans-serif;font-size:14px;text-decoration:none}
.brand{position:absolute;left:0;width:1200px;text-align:center;color:var(--white)}
.brand .name{font-family:"Montserrat",sans-serif;font-size:16px;letter-spacing:3px;font-weight:500;white-space:nowrap}
.brand .sub{font-family:"Montserrat",sans-serif;font-size:8px;letter-spacing:4px}
.hero-title{position:absolute;top:410px;width:1200px;text-align:center;color:#f5ead6;font-size:70px}
.hero-sub{position:absolute;top:500px;width:1200px;text-align:center;color:var(--white);font-size:14px}
.play{position:absolute;border:2px solid rgba(255,255,255,.85);border-radius:50%}

/* section headings */
.eyebrow{font-family:"Montserrat",sans-serif;font-size:16px;letter-spacing:6px;color:var(--gold);text-transform:uppercase}
.heading{font-family:"Montserrat",sans-serif;font-size:29px;letter-spacing:8px;font-weight:500;text-transform:uppercase;white-space:nowrap}
.center{left:0;width:1200px;text-align:center}

/* about */
.about-arch{left:155px;top:845px;width:393px;height:490px;border-radius:196px 196px 0 0;background:linear-gradient(180deg,#a68b4c,#8f773f)}
.about-photo{left:230px;top:845px;width:240px;height:490px;background:linear-gradient(180deg,#5a4a3d 0%,#2f6a55 55%,#1f4f41 100%);border-radius:110px 110px 0 0}
.about-base{left:155px;top:1333px;width:393px;height:12px;background:var(--brown);border-radius:3px}
.about-text p{font-size:12.5px;line-height:30px;color:var(--text);margin-bottom:30px}
.btn-outline{position:absolute;border:2px solid var(--brown);border-radius:8px;font-family:"Montserrat",sans-serif;font-size:13px;letter-spacing:4px;text-transform:uppercase;display:flex;align-items:center;justify-content:center;color:var(--brown)}

/* portfolio */
.portfolio{left:0;top:1495px;width:1200px;height:823px;background:var(--gold)}
.film{position:absolute;border-radius:8px;overflow:hidden}
.film .couple{position:absolute;left:0;width:100%;text-align:center;color:var(--white);font-family:"Montserrat",sans-serif;font-size:18px;letter-spacing:8px;text-transform:uppercase;white-space:nowrap}
.film .venue{position:absolute;left:0;width:100%;text-align:center;color:var(--white);font-size:11px;text-transform:uppercase}

/* packages */
.card{position:absolute;top:2492px;width:304px;height:468px;border-radius:18px;background:var(--cream);box-shadow:0 3px 12px rgba(0,0,0,.12);overflow:hidden}
.card .head{height:112px;background:var(--brown);color:var(--white);text-align:center;padding-top:32px}
.card .head .small{font-family:"Montserrat",sans-serif;font-size:12px;letter-spacing:3px}
.card .head .big{font-family:"Montserrat",sans-serif;font-size:22px;letter-spacing:5px;font-weight:500;margin-top:4px}
.card .wave{display:block}
.card .body{padding:20px 42px 0;text-align:center;font-size:13.5px;line-height:17.5px;color:var(--text)}
.card .body p{margin-bottom:18px}
.card .price{position:absolute;left:38px;bottom:25px;width:228px;height:52px;border-radius:10px;background:var(--brown);color:var(--white);font-family:"Montserrat",sans-serif;font-weight:600;font-size:17px;display:flex;align-items:center;justify-content:center}
.card.featured{background:var(--brown)}
.card.featured .head{background:var(--gold)}
.card.featured .body{color:#f1ebe0}
.card.featured .price{background:var(--gold)}

/* testimonials */
.testimonials{left:0;top:3075px;width:1200px;height:675px;background:linear-gradient(100deg,#5d4a3c 0%,#7a6552 35%,#8d7a69 60%,#5e5148 100%)}
.testi-text{left:160px;top:3425px;width:470px;color:#f3ece1;font-size:11.5px;line-height:30px}

/* instagram */
.tile{position:absolute;border-radius:6px}

/* footer */
.footer{left:0;top:4500px;width:1200px;height:360px;background:var(--brown)}
.footer h4{font-family:"Montserrat",sans-serif;font-weight:500;font-size:17px;letter-spacing:6px;color:var(--gold)}
.links li{list-style:none;color:var(--white);font-size:13px;line-height:23px}
.links li::before{content:"› ";}
.foot-txt{color:var(--white);font-size:13px}
.field{position:absolute;left:850px;top:4690px;width:277px;height:44px;background:var(--white);border-radius:8px;font-size:12px;color:#b9b1a6;padding:15px 16px}
.subscribe{position:absolute;left:850px;top:4748px;width:277px;height:44px;background:var(--gold);border-radius:8px;font-family:"Montserrat",sans-serif;font-size:12px;letter-spacing:4px;color:var(--brown);display:flex;align-items:center;justify-content:center}
.bottom-bar{left:0;top:4860px;width:1200px;height:70px;background:var(--cream)}
.social{position:absolute;top:4880px;width:30px;height:30px;border-radius:50%;background:var(--gold)}
</style>
</head>
<body>

<!-- HERO -->
<section class="hero" role="img" aria-label="Bride and groom holding hands with a pink rose bouquet"></section>
<nav class="nav">
  <a style="left:193px">About</a>
  <a style="left:287px">Films</a>
  <a style="left:372px">Options</a>
  <a style="left:780px">Reviews</a>
  <a style="left:888px">Prices</a>
  <a style="left:980px">Contact</a>
</nav>
<div class="brand" style="top:88px"><div class="name">CORIN BRENNOLFSIDE</div><div class="sub">WEDDING FILMS</div></div>
<div class="play" style="left:583px;top:364px;width:36px;height:36px">
  <svg width="32" height="32" viewBox="0 0 32 32"><path d="M13 10 L22 16 L13 22 Z" fill="none" stroke="#fff" stroke-width="1.6"/></svg>
</div>
<div class="hero-title script">Corin Brennolfside</div>
<div class="hero-sub">North East and Yorkshire Wedding Videographer</div>
<svg class="abs" style="left:540px;top:672px" width="120" height="40" viewBox="0 0 120 40"><path d="M0 40 C30 40 38 0 60 0 C82 0 90 40 120 40 Z" fill="#fdfaf1"/><circle cx="60" cy="25" r="5" fill="none" stroke="#a68b4c" stroke-width="2"/></svg>

<!-- ABOUT -->
<div class="abs about-arch"></div>
<div class="abs about-photo" role="img" aria-label="Portrait of the filmmaker in a hat and green jumper"></div>
<div class="abs about-base"></div>
<div class="abs eyebrow" style="left:628px;top:888px">About</div>
<div class="abs heading" style="left:628px;top:910px;color:var(--brown);letter-spacing:6px">Corin Brennolfside</div>
<div class="abs about-text" style="left:628px;top:963px;width:470px">
  <p>I'm a filmmaker who loves documenting couples' most important day of their lives. Based in County Durham I film weddings mostly in the North East of England however regularly travel around the UK and Europe.</p>
  <p>I first picked up a video camera when I was 8 years old making home movies documenting family holidays and events and it led me onto gaining a degree in TV and Radio Production at University. After University I set up my own small film company which led to many opportunities including filming events and stories across the North East and further afield.</p>
</div>
<div class="btn-outline" style="left:634px;top:1277px;width:205px;height:61px">Read More</div>

<!-- PORTFOLIO -->
<section class="abs portfolio"></section>
<div class="abs center" style="top:1548px;color:var(--white);font-family:Montserrat,sans-serif;font-size:16px;letter-spacing:6px">VIDEOS</div>
<div class="abs heading center" style="top:1570px;color:var(--white)">Portfolio</div>

<div class="film" style="left:115px;top:1635px;width:312px;height:240px;background:linear-gradient(160deg,#6a3d24,#b06a3a 55%,#3b2a20)" role="img" aria-label="Couple beside a vintage orange van">
  <div class="couple" style="top:170px">Isla + Tomas</div><div class="venue" style="top:200px">Villa Serrano, Umbria, Italy</div></div>
<div class="film" style="left:447px;top:1635px;width:310px;height:500px;background:linear-gradient(180deg,#3c3c3c,#8b8b86 45%,#d9d6d0 80%,#9c9890)" role="img" aria-label="Couple embracing under a bridge, bride in a full white gown">
  <div class="play" style="left:137px;top:240px;width:36px;height:36px"><svg width="32" height="32" viewBox="0 0 32 32"><path d="M13 10 L22 16 L13 22 Z" fill="none" stroke="#fff" stroke-width="1.6"/></svg></div>
  <div class="couple" style="top:430px">Maisie + Rowan</div><div class="venue" style="top:462px">Harlow Mill Inn, Durham</div></div>
<div class="film" style="left:777px;top:1635px;width:311px;height:240px;background:linear-gradient(160deg,#3d5a2f,#84a06a 50%,#2e3f26)" role="img" aria-label="Couple in a leafy garden">
  <div class="couple" style="top:170px">Freya + Dominic</div><div class="venue" style="top:200px">Ashgrove Manor, Leicestershire</div></div>
<div class="film" style="left:115px;top:1895px;width:312px;height:240px;background:linear-gradient(160deg,#4b3b2e,#a28a6d 50%,#d5cbbd)" role="img" aria-label="Couple on a city street at dusk">
  <div class="couple" style="top:170px">Nell + Oscar</div><div class="venue" style="top:200px">Elmbrook Hall Wedding</div></div>
<div class="film" style="left:777px;top:1895px;width:311px;height:240px;background:linear-gradient(180deg,#8da3a9,#c9c1b2 55%,#d8cdbb)" role="img" aria-label="Groom carrying bride on a beach by sea stacks">
  <div class="couple" style="top:170px">Isla + Tomas</div><div class="venue" style="top:200px">Villa Serrano, Umbria, Italy</div></div>
<div class="btn-outline" style="left:509px;top:2183px;width:204px;height:61px;border-color:var(--white);color:var(--white);font-size:12px">Read More</div>

<!-- PACKAGES -->
<div class="abs eyebrow center" style="top:2404px">Our</div>
<div class="abs heading center" style="top:2428px;color:var(--brown)">Package</div>

<div class="card" style="left:115px">
  <div class="head"><div class="small">GOLD</div><div class="big">WEDDING FILM</div></div>
  <svg class="wave" width="304" height="10" viewBox="0 0 304 10" preserveAspectRatio="none"><path d="M0 0 H304 V2 Q296 10 288 2 Q280 10 272 2 Q264 10 256 2 Q248 10 240 2 Q232 10 224 2 Q216 10 208 2 Q200 10 192 2 Q184 10 176 2 Q168 10 160 2 Q152 10 144 2 Q136 10 128 2 Q120 10 112 2 Q104 10 96 2 Q88 10 80 2 Q72 10 64 2 Q56 10 48 2 Q40 10 32 2 Q24 10 16 2 Q8 10 0 2 Z" fill="#3e342d"/></svg>
  <div class="body"><p>My signature package includes coverage from 2 hours before the ceremony to 15 minutes after the first dance (max 8.30pm).</p><p>You will receive a highlights film of your wedding day featuring audio, plus the full ceremony and speeches filmed with 3 cameras.</p><p>Your wedding films will be delivered digitally.</p></div>
  <div class="price">FROM £1,500</div>
</div>
<div class="card featured" style="left:448px">
  <div class="head"><div class="small">WEDDING</div><div class="big">PHOTOGRAPHY</div></div>
  <svg class="wave" width="304" height="10" viewBox="0 0 304 10" preserveAspectRatio="none"><path d="M0 0 H304 V2 Q296 10 288 2 Q280 10 272 2 Q264 10 256 2 Q248 10 240 2 Q232 10 224 2 Q216 10 208 2 Q200 10 192 2 Q184 10 176 2 Q168 10 160 2 Q152 10 144 2 Q136 10 128 2 Q120 10 112 2 Q104 10 96 2 Q88 10 80 2 Q72 10 64 2 Q56 10 48 2 Q40 10 32 2 Q24 10 16 2 Q8 10 0 2 Z" fill="#a68b4c"/></svg>
  <div class="body"><p>Add wedding photography onto your package.</p><p>This includes coverage from 2.5 hours before the wedding ceremony to shortly after the first dance.</p><p>A minimum of 700 photographs are provided on USB memory stick and as a digital download.</p></div>
  <div class="price">FROM &nbsp;£700</div>
</div>
<div class="card" style="left:784px">
  <div class="head"><div class="small">FILM</div><div class="big">ENGAGEMEN</div></div>
  <svg class="wave" width="304" height="10" viewBox="0 0 304 10" preserveAspectRatio="none"><path d="M0 0 H304 V2 Q296 10 288 2 Q280 10 272 2 Q264 10 256 2 Q248 10 240 2 Q232 10 224 2 Q216 10 208 2 Q200 10 192 2 Q184 10 176 2 Q168 10 160 2 Q152 10 144 2 Q136 10 128 2 Q120 10 112 2 Q104 10 96 2 Q88 10 80 2 Q72 10 64 2 Q56 10 48 2 Q40 10 32 2 Q24 10 16 2 Q8 10 0 2 Z" fill="#3e342d"/></svg>
  <div class="body"><p>My signature package includes coverage from 2 hours before the ceremony to 15 minutes after the first dance (max 8.30pm).</p><p>You will receive a highlights film of your wedding day featuring audio, plus the full ceremony and speeches filmed with 3 cameras.</p><p>Your wedding films will be delivered digitally.</p></div>
  <div class="price">FROM £200</div>
</div>

<!-- TESTIMONIALS -->
<section class="abs testimonials" role="img" aria-label="Bride in a flowing white gown on a rocky coastline"></section>
<div class="abs eyebrow center" style="top:3150px;color:var(--gold-light)">Client's</div>
<div class="abs heading center" style="top:3172px;color:var(--white)">Testimonials</div>
<div class="play" style="left:885px;top:3420px;width:38px;height:38px"><svg width="34" height="34" viewBox="0 0 34 34"><path d="M14 11 L23 17 L14 23 Z" fill="none" stroke="#fff" stroke-width="1.6"/></svg></div>
<div class="abs script" style="left:150px;top:3290px;color:var(--white);font-size:72px;white-space:nowrap">Harriet Loxley</div>
<div class="abs caps" style="left:162px;top:3398px;color:var(--white);font-size:13px;letter-spacing:4px">Umbria, Italy</div>
<div class="abs testi-text">Absolutely amazing videographer! What can we say, our short film captures our day perfectly and includes everything we wanted. Both Corin and Elliot were most professional and easy to work with on the day. They captured moments that I wouldn't have seen otherwise (like groom panicking beforehand). Would highly recommend!</div>
<svg class="abs" style="left:160px;top:3615px" width="90" height="8" viewBox="0 0 90 8"><rect x="0" y="1" width="8" height="5" rx="2" fill="#fff"/><rect x="22" y="1" width="36" height="5" rx="2" fill="#a68b4c"/><rect x="68" y="1" width="8" height="5" rx="2" fill="#fff"/><rect x="80" y="1" width="8" height="5" rx="2" fill="#fff"/></svg>

<!-- INSTAGRAM -->
<div class="abs eyebrow center" style="top:3832px">Follow us</div>
<div class="abs heading center" style="top:3854px;color:var(--brown)">Instagram</div>
<div class="tile" style="left:115px;top:3922px;width:233px;height:218px;background:linear-gradient(160deg,#2a2522,#5a4a3c 60%,#1e1b19)" role="img" aria-label="Wedding trailer film still, couple in dark tones"></div>
<div class="tile" style="left:364px;top:3922px;width:231px;height:218px;background:linear-gradient(160deg,#8e8f95,#d2ccc5 60%,#777)" role="img" aria-label="Couple kissing in wedding attire"></div>
<div class="tile" style="left:608px;top:3922px;width:481px;height:218px;background:linear-gradient(100deg,#5b4b3f,#a69585 50%,#d7cfc6)" role="img" aria-label="Bride with long gown spread on the rocks"></div>
<div class="tile" style="left:115px;top:4156px;width:480px;height:219px;background:linear-gradient(180deg,#9aa0a3,#6d6f70 55%,#2b2b2b)" role="img" aria-label="Couple on a black sand beach beside sea stacks"></div>
<div class="tile" style="left:608px;top:4156px;width:234px;height:219px;background:linear-gradient(180deg,#c9c2b8,#8a7e70 60%,#55493f)" role="img" aria-label="Couple walking down a narrow stone lane"></div>
<div class="tile" style="left:856px;top:4156px;width:233px;height:219px;background:linear-gradient(160deg,#1e1b19,#4a3f36 60%,#181614)" role="img" aria-label="Wedding film still with guests in hats"></div>

<!-- FOOTER -->
<footer class="abs footer"></footer>
<div class="abs" style="left:40px;top:4694px;width:250px;text-align:center;color:var(--gold)">
  <div style="font-family:Montserrat,sans-serif;font-size:14px;letter-spacing:3px;white-space:nowrap">CORIN BRENNOLFSIDE</div>
  <div style="font-family:Montserrat,sans-serif;font-size:8px;letter-spacing:4px;margin-top:4px">WEDDING FILMS</div>
</div>
<h4 class="abs" style="left:380px;top:4596px">LINK</h4>
<ul class="abs links" style="left:365px;top:4636px">
  <li>Home</li><li>Meet Corin</li><li>Videos</li><li>Packages</li><li>Testimionials</li><li>Blog</li><li>Contact</li>
</ul>
<h4 class="abs" style="left:590px;top:4596px">CONTACT</h4>
<svg class="abs" style="left:568px;top:4644px" width="12" height="12" viewBox="0 0 24 24"><path d="M6 2 L10 2 L11 7 L8 9 C9 12 12 15 15 16 L17 13 L22 14 L22 18 C22 20 20 22 18 22 C9 21 3 15 2 6 C2 4 4 2 6 2 Z" fill="#fff"/></svg>
<div class="abs foot-txt" style="left:590px;top:4642px">07700 900 318</div>
<svg class="abs" style="left:568px;top:4684px" width="12" height="10" viewBox="0 0 24 18"><rect x="1" y="1" width="22" height="16" fill="none" stroke="#fff" stroke-width="2"/><path d="M1 1 L12 10 L23 1" fill="none" stroke="#fff" stroke-width="2"/></svg>
<div class="abs foot-txt" style="left:593px;top:4680px">films@brennolfside.com</div>
<div class="abs" style="left:597px;top:4725px;width:72px;height:72px;border-radius:50%;background:var(--white)"></div>
<div class="abs" style="left:682px;top:4725px;width:72px;height:72px;border-radius:50%;background:#f2e59a;border:3px solid var(--gold)"></div>
<h4 class="abs" style="left:850px;top:4596px">NEWSLETTER</h4>
<div class="abs foot-txt" style="left:850px;top:4638px;width:280px;line-height:17px">Keep up our latest news and events. Subscribe our newsletter</div>
<div class="field">Email Address...</div>
<div class="subscribe">SUBSCRIBE</div>

<section class="abs bottom-bar"></section>
<div class="abs" style="left:73px;top:4888px;font-size:11px;color:var(--brown)">COPYRIGHT © 2022 <b>CORIN BRENNOLFSIDE</b></div>
<div class="abs" style="left:395px;top:4888px;font-size:11px;color:var(--brown)">WEDDING VIDEOGRAPHY - NORTH EAST, UK AND WORLDWIDE FILM</div>
<div class="social" style="left:1022px"></div>
<div class="social" style="left:1059px;background:var(--brown)"></div>
<div class="social" style="left:1096px;background:var(--brown)"></div>

</body>
</html>
```